IT Company based on Biology Business Needs a Business Card Design

We need a business card design for a new company called 'Lumen CELL'. We develop the machine learning solutions especially focused on deep learning algorithms for biology industry. Our initial product is a vision detection on biological images to help doctors diagnose the symptoms. We would like to see designs that use the color green.

Industry/Entity Type

Business

```html
<!DOCTYPE html>
<html lang="en">
<head>
<meta charset="utf-8">
<title>Lumen CELL – Business Card</title>
<link rel="stylesheet" href="https://fonts.googleapis.com/css2?family=Open+Sans:wght@400;600;700&display=swap">
<style>
  :root {
    --green: #17a850;
    --green-light: #1dbb5e;
    --green-dark: #0f8f40;
    --lime: #8ccf3a;
    --paper: #f7f7f5;
    --white: #ffffff;
    --stage: #e9ebe7;
  }
  * { margin: 0; padding: 0; box-sizing: border-box; }
  html, body { width: 1200px; height: 780px; overflow: hidden; }
  body {
    background: var(--stage);
    font-family: "Open Sans", Arial, sans-serif;
    display: flex;
    align-items: center;
    justify-content: center;
    gap: 60px;
  }
  .card {
    position: relative;
    width: 525px;
    height: 300px;
    border-radius: 4px;
    overflow: hidden;
    box-shadow: 0 10px 28px rgba(0,0,0,.18);
  }
  .card-front { background: var(--paper); }
  .front-band { position: absolute; inset: 0; width: 100%; height: 100%; }
  .brand {
    position: absolute;
    display: flex;
    align-items: center;
    gap: 10px;
    font-weight: 600;
    letter-spacing: 1px;
    white-space: nowrap;
  }
  .brand-dot { width: 12px; height: 12px; border-radius: 50%; flex: none; }
  .card-front .brand { left: 28px; top: 132px; font-size: 28px; line-height: 36px; color: var(--green); }
  .card-front .brand-dot { background: var(--green); }
  .contact {
    position: absolute;
    left: 312px;
    top: 52px;
    color: var(--white);
    font-size: 13px;
    line-height: 1.35;
    white-space: nowrap;
  }
  .person-name { font-weight: 700; font-size: 17px; letter-spacing: .5px; }
  .person-role { font-size: 13px; margin-bottom: 18px; }
  .address { margin-bottom: 14px; }
  .contact-line { display: flex; align-items: center; gap: 8px; }
  .contact-icon {
    width: 14px; height: 14px;
    background: var(--white);
    border-radius: 2px;
    display: inline-flex; align-items: center; justify-content: center;
  }
  .website { margin-top: 8px; }
  .card-back {
    background: radial-gradient(ellipse at 40% 40%, var(--green-light), var(--green) 60%, var(--green-dark));
  }
  .card-back .brand {
    left: 50%; top: 50%;
    transform: translate(-50%, -50%);
    font-size: 46px;
    color: var(--white);
  }
  .card-back .brand-dot { background: var(--white); width: 18px; height: 18px; }
</style>
</head>
<body>
  <section class="card card-front">
    <svg class="front-band" viewBox="0 0 525 300" preserveAspectRatio="none" aria-hidden="true">
      <path d="M300 0 C 264 110, 256 200, 280 300 L525 300 L525 0 Z" fill="#8ccf3a"/>
      <path d="M310 0 C 274 110, 266 200, 292 300 L525 300 L525 0 Z" fill="#17a850"/>
    </svg>
    <div class="brand"><span class="brand-dot"></span>Lumen CELL</div>
    <div class="contact">
      <p class="person-name">EMPLOYEE NAME</p>
      <p class="person-role">Managing Director</p>
      <p class="address">0000 Meadow Lane<br>Fernvale, OR 0000</p>
      <p class="contact-line">
        <span class="contact-icon"><svg width="10" height="10" viewBox="0 0 10 10"><path d="M2 1 L4 1 L4.5 3 L3.5 4 Q4.5 6 6 6.5 L7 5.5 L9 6 L9 8 Q5 9 2 6 Q1 4 2 1Z" fill="#17a850"/></svg></span>000-111-0000
      </p>
      <p class="contact-line">
        <span class="contact-icon"><svg width="10" height="10" viewBox="0 0 10 10"><rect x="1" y="3" width="8" height="5" fill="#17a850"/><rect x="3" y="1" width="4" height="2" fill="#17a850"/></svg></span>000-111-0000
      </p>
      <p class="contact-line">
        <span class="contact-icon"><svg width="10" height="10" viewBox="0 0 10 10"><rect x="1" y="2.5" width="8" height="5.5" fill="none" stroke="#17a850" stroke-width="1.2"/><path d="M1 2.5 L5 6 L9 2.5" fill="none" stroke="#17a850" stroke-width="1.2"/></svg></span>hello@lumencell.io
      </p>
      <p class="website">www.lumencell.io</p>
    </div>
  </section>

  <section class="card card-back">
    <div class="brand"><span class="brand-dot"></span>Lumen CELL</div>
  </section>
</body>
</html>
```